VitaLern
Lifeline Instruction
Simple
Ted Marwick
Owner
287 Felcourt Lane Brindlewood, New Fenwick 00000
Ted@VitaLern.com
www.VitaLern.com
Healthcare education and consulting.

```html
<!DOCTYPE html>
<html lang="en">
<head>
<meta charset="utf-8">
<title>VitaLern Business Card</title>
<link rel="stylesheet" href="https://fonts.googleapis.com/css2?family=Rubik:wght@400;500&family=Roboto+Slab:wght@300;400;700&display=swap">
<style>
  :root {
    --backdrop: #d9d9d9;
    --maroon: #7d231c;
    --accent: #e0483e;
    --white: #ffffff;
    --ink: #6b6b6b;
    --rule: #c9c9c9;
    --band-gray: #e6e6e6;
  }
  * { margin: 0; padding: 0; box-sizing: border-box; }
  html, body { width: 1200px; height: 901px; overflow: hidden; }
  body {
    background: var(--backdrop);
    position: relative;
    font-family: "Roboto Slab", serif;
  }
  .card {
    position: absolute;
    left: 299px;
    width: 601px;
    height: 341px;
    border-radius: 22px;
    overflow: hidden;
  }
  .card-front { top: 68px; background: var(--maroon); }
  .card-back { top: 487px; background: var(--white); }

  .brand { position: absolute; display: flex; align-items: center; }
  .brand-dot { border-radius: 50%; flex: none; }
  .brand-name { font-family: "Rubik", sans-serif; font-weight: 400; line-height: 1; }
  .brand-tagline { font-family: "Rubik", sans-serif; font-weight: 400; line-height: 1; }

  .card-front .brand { left: 78px; top: 100px; }
  .card-front .brand-dot { width: 92px; height: 92px; background: var(--white); margin-right: 38px; }
  .card-front .brand-name { font-size: 44px; color: var(--white); }
  .card-front .brand-tagline { font-size: 27px; color: var(--white); margin-top: 8px; }

  .front-slogan {
    position: absolute; left: 0; right: 0; top: 307px;
    text-align: center; color: var(--white);
    font-size: 15px; font-weight: 400;
  }

  .card-back .brand { left: 34px; top: 138px; }
  .card-back .brand-dot { width: 52px; height: 52px; background: var(--accent); margin-right: 20px; }
  .card-back .brand-name { font-size: 25px; color: var(--accent); }
  .card-back .brand-tagline { font-size: 17px; color: var(--accent); margin-top: 5px; }

  .divider {
    position: absolute; left: 302px; top: 73px;
    width: 1px; height: 195px; background: var(--rule);
  }
  .contact { position: absolute; left: 322px; top: 78px; color: var(--ink); }
  .contact-name { font-size: 25px; font-weight: 700; color: var(--accent); line-height: 1; }
  .contact-role { font-size: 12px; margin-top: 7px; }
  .contact-address { font-size: 13.5px; line-height: 20px; margin-top: 20px; }
  .contact-list { list-style: none; margin-top: 16px; }
  .contact-list li {
    display: flex; align-items: center;
    font-size: 13.5px; line-height: 19.5px;
  }
  .contact-list svg { width: 11px; height: 11px; margin-right: 9px; fill: var(--accent); flex: none; }

  .back-band { position: absolute; left: 0; bottom: 0; width: 100%; height: 20px; }
</style>
</head>
<body>

<section class="card card-front">
  <div class="brand">
    <span class="brand-dot"></span>
    <div>
      <div class="brand-name">VitaLern</div>
      <div class="brand-tagline">Lifeline Instruction</div>
    </div>
  </div>
  <p class="front-slogan">Healthcare Education and Consulting</p>
</section>

<section class="card card-back">
  <div class="brand">
    <span class="brand-dot"></span>
    <div>
      <div class="brand-name">VitaLern</div>
      <div class="brand-tagline">Lifeline Instruction</div>
    </div>
  </div>

  <div class="divider"></div>

  <div class="contact">
    <h1 class="contact-name">TED MARWICK</h1>
    <p class="contact-role">Owner</p>
    <p class="contact-address">287 Felcourt Lane Brindlewood,<br>New Fenwick 00000</p>
    <ul class="contact-list">
      <li><svg viewBox="0 0 12 12"><path d="M2 1h2.5l1 3-1.5 1a6 6 0 0 0 3 3l1-1.5 3 1V10a1.5 1.5 0 0 1-1.5 1.5A9.5 9.5 0 0 1 .5 2.5 1.5 1.5 0 0 1 2 1z"/></svg>555-010-0142</li>
      <li><svg viewBox="0 0 12 12"><path d="M3 0h6a1 1 0 0 1 1 1v10a1 1 0 0 1-1 1H3a1 1 0 0 1-1-1V1a1 1 0 0 1 1-1zm.8 1.5v7.5h4.4V1.5z"/></svg>555-010-0187</li>
      <li><svg viewBox="0 0 12 12"><path d="M0 2.5h12v7H0zM1 3.3l5 3.4 5-3.4v-.1H1z"/></svg>Ted@VitaLern.com</li>
      <li><svg viewBox="0 0 12 12"><circle cx="6" cy="6" r="5.5"/></svg>www.VitaLern.com</li>
    </ul>
  </div>

  <svg class="back-band" viewBox="0 0 601 20" preserveAspectRatio="none">
    <rect x="0" y="4" width="601" height="16" fill="var(--band-gray)"/>
    <polygon points="0,4 300,4 290,20 0,20" fill="var(--accent)"/>
  </svg>
</section>

</body>
</html>
```